Yard Sign Design Needed

Yard sign needed for mowing & landscaping company. Would like to use the top logo with black background which is attached. Would like MOWING to be in large standout letters. The word "landscaping" can be smaller and more artistic or omitted. Will need room for phone number once design is approved. The phone number will need to stand out and look identical/similar to the word 'MOWING"

```html
<!DOCTYPE html>
<html lang="en">
<head>
<meta charset="UTF-8">
<title>Talven Contractors – Mowing Yard Sign</title>
<link href="https://fonts.googleapis.com/css2?family=Archivo+Black&family=Archivo:wght@700&display=swap" rel="stylesheet">
<style>
  :root {
    --backdrop: #858181;
    --sign-black: #000000;
    --grass-green: #88a300;
    --paper-white: #ffffff;
  }
  * { margin: 0; padding: 0; box-sizing: border-box; }
  html, body {
    width: 959px;
    height: 1200px;
    overflow: hidden;
    background: var(--backdrop);
  }
  .canvas {
    position: relative;
    width: 959px;
    height: 1200px;
  }
  .yard-sign {
    position: absolute;
    left: 30px;
    top: 267px;
    width: 900px;
    height: 666px;
    background: var(--sign-black);
    overflow: hidden;
  }
  .brand {
    position: absolute;
    top: 48px;
    left: 0;
    width: 100%;
    display: flex;
    justify-content: center;
    align-items: center;
    gap: 26px;
  }
  .brand-mark {
    width: 110px;
    height: 110px;
    background: var(--grass-green);
  }
  .brand-name {
    font-family: "Archivo Black", sans-serif;
    color: var(--grass-green);
    line-height: 1;
    text-transform: uppercase;
  }
  .brand-name .primary {
    display: block;
    font-size: 74px;
    letter-spacing: 0.02em;
  }
  .brand-name .secondary {
    display: block;
    font-size: 31px;
    letter-spacing: 0.04em;
    margin-top: 10px;
  }
  .service-main {
    position: absolute;
    top: 262px;
    width: 100%;
    text-align: center;
    font-family: "Archivo Black", sans-serif;
    font-size: 150px;
    line-height: 1;
    color: var(--grass-green);
    letter-spacing: -0.02em;
  }
  .service-sub {
    position: absolute;
    top: 408px;
    width: 100%;
    text-align: center;
    font-family: "Archivo", sans-serif;
    font-weight: 700;
    font-size: 54px;
    line-height: 1;
    color: var(--paper-white);
    letter-spacing: 0.5em;
    padding-left: 0.5em;
  }
  .grass-edge {
    position: absolute;
    top: 482px;
    left: 0;
    width: 100%;
    height: 50px;
    background: linear-gradient(to bottom, var(--sign-black), var(--paper-white));
  }
  .contact-panel {
    position: absolute;
    top: 532px;
    left: 0;
    width: 100%;
    height: 134px;
    background: var(--paper-white);
    display: flex;
    align-items: center;
    justify-content: center;
  }
  .phone {
    font-family: "Archivo Black", sans-serif;
    font-size: 82px;
    line-height: 1;
    color: var(--grass-green);
    letter-spacing: 0.01em;
  }
</style>
</head>
<body>
  <main class="canvas">
    <section class="yard-sign">
      <header class="brand">
        <div class="brand-mark"></div>
        <div class="brand-name">
          <span class="primary">Talven</span>
          <span class="secondary">Contractors LLC</span>
        </div>
      </header>
      <h1 class="service-main">MOWING</h1>
      <p class="service-sub">LANDSCAPING</p>
      <div class="grass-edge" role="img" aria-label="White grass blade silhouette edge rising into the black area"></div>
      <footer class="contact-panel">
        <p class="phone">CALL : 20030 418</p>
      </footer>
    </section>
  </main>
</body>
</html>
```